RK LAW
Stationary Envelopes and Cards
RK LAW - Law
Creative Brief
Professional
Howard P. Lindqvist
Attorney At Law
347 N. 4th Avenue Las Vegas NV 89104
nvrklaw@mailbrook.net
NVRKLAW.NET

```html
<!DOCTYPE html>
<html lang="en">
<head>
<meta charset="utf-8">
<title>RK LAW – Business Cards</title>
<link href="https://fonts.googleapis.com/css2?family=Cinzel:wght@400&display=swap" rel="stylesheet">
<style>
  :root {
    --page: #ffffff;
    --card-edge: #b9b9b9;
    --blue-deep: #0a5fb4;
    --blue-mid: #1a86d6;
    --blue-light: #22aef0;
    --wave-pale: #cfe9f8;
    --gold-light: #f3d98c;
    --gold-deep: #c8993e;
    --text-blue: #1d6fbf;
    --text-dark: #333333;
    --white: #ffffff;
  }
  * { margin: 0; padding: 0; box-sizing: border-box; }
  html, body { width: 1200px; height: 727px; overflow: hidden; background: var(--page); }
  .sheet { position: relative; width: 1200px; height: 727px; font-family: "Cinzel", "Times New Roman", serif; }

  .card { position: absolute; width: 554px; height: 306px; overflow: hidden; }
  .card--front { left: 43px; top: 43px; background: var(--white); border: 1px solid var(--card-edge); }
  .card--blue { left: 605px; top: 43px; background: linear-gradient(115deg, var(--blue-light) 0%, var(--blue-mid) 50%, var(--blue-deep) 100%); }
  .card--white { left: 43px; top: 367px; background: var(--white); border: 1px solid var(--card-edge); }
  .card--gold { left: 605px; top: 367px; background: linear-gradient(120deg, var(--gold-deep) 0%, var(--gold-light) 45%, var(--gold-deep) 100%); }

  .wordmark { position: absolute; display: flex; align-items: center; gap: 12px; }
  .wordmark__square { width: 22px; height: 22px; background: currentColor; flex: none; }
  .wordmark__name { font-size: 30px; font-weight: 400; line-height: 1; letter-spacing: 1px; }

  .card--front .wordmark { left: 26px; top: 44px; color: var(--text-blue); }
  .wordmark--centered { left: 50%; top: 50%; transform: translate(-50%, -50%); }
  .card--blue .wordmark { color: var(--white); }
  .card--white .wordmark { color: var(--text-blue); }
  .card--gold .wordmark { color: var(--white); }

  .person { position: absolute; left: 230px; right: 24px; top: 136px; text-align: center; }
  .person__name { font-size: 23px; line-height: 1.2; color: var(--text-blue); }
  .person__title { font-size: 12.5px; color: var(--text-dark); margin-top: 4px; }

  .wave { position: absolute; left: 0; top: 0; width: 554px; height: 306px; }

  .contact { position: absolute; left: 24px; top: 226px; color: var(--white); font-size: 10.5px; line-height: 15px; font-style: normal; }
</style>
</head>
<body>
<main class="sheet">

  <section class="card card--front" aria-label="Business card front">
    <svg class="wave" viewBox="0 0 554 306" aria-hidden="true">
      <defs>
        <linearGradient id="waveFill" x1="0" y1="0" x2="1" y2="0">
          <stop offset="0" stop-color="#22aef0"/>
          <stop offset="1" stop-color="#0a5fb4"/>
        </linearGradient>
      </defs>
      <path d="M0 200 C 140 160 300 255 554 160 L554 306 L0 306 Z" fill="#cfe9f8"/>
      <path d="M0 212 C 150 176 310 268 554 174 L554 306 L0 306 Z" fill="url(#waveFill)"/>
    </svg>
    <div class="wordmark">
      <span class="wordmark__square"></span>
      <span class="wordmark__name">RK LAW</span>
    </div>
    <div class="person">
      <p class="person__name">Howard P. Lindqvist</p>
      <p class="person__title">Attorney At Law</p>
    </div>
    <address class="contact">
      347 N. 4th Avenue, Las Vegas NV 89104<br>
      Phone: (702) 555-0187 | Fax: (702) 555-0192<br>
      Email: nvrklaw@mailbrook.net<br>
      www.NVRKLAW.NET
    </address>
  </section>

  <section class="card card--blue" aria-label="Business card back, blue">
    <div class="wordmark wordmark--centered">
      <span class="wordmark__square"></span>
      <span class="wordmark__name">RK LAW</span>
    </div>
  </section>

  <section class="card card--white" aria-label="Business card back, white">
    <div class="wordmark wordmark--centered">
      <span class="wordmark__square"></span>
      <span class="wordmark__name">RK LAW</span>
    </div>
  </section>

  <section class="card card--gold" aria-label="Business card back, gold">
    <div class="wordmark wordmark--centered">
      <span class="wordmark__square"></span>
      <span class="wordmark__name">RK LAW</span>
    </div>
  </section>

</main>
</body>
</html>
```